Professional letterhead for engineering type firm.

I would like to have a professional looking letterhead for a small HVAC testing company/engineering-type firm. I would like to see designs that show a professional level of expertise and established company. Traditional letterhead designs are a good place to start.
We are a KVSD certified company (which is a big deal in our industry). I have included the KVSD logo, but would like the green in KVSD logo to be black.
Presently, we work out of house so i would not like to include our address at this point.
Information to include:
Phone: 555-203-4617
Website: www.Morvex-QSD.com
Email: Info@Morvex-QSD.com

```html
<!DOCTYPE html>
<html lang="en">
<head>
<meta charset="utf-8">
<title>Morvex QSD Letterhead</title>
<link href="https://fonts.googleapis.com/css2?family=Lato:wght@400;700&family=Montserrat:wght@400;500&family=Great+Vibes&display=swap" rel="stylesheet">
<style>
  :root {
    --backdrop: #e7e8ea;
    --paper: #ffffff;
    --ink: #1d1d1f;
    --muted: #3a3a3c;
    --brand-red: #ec1c24;
    --brand-blue: #2b3f94;
    --badge: #111111;
  }
  * { margin: 0; padding: 0; box-sizing: border-box; }
  html, body { width: 1200px; height: 874px; overflow: hidden; }
  body {
    background: var(--backdrop);
    font-family: "Lato", Arial, sans-serif;
    color: var(--ink);
    position: relative;
  }
  .letterhead {
    position: absolute;
    left: 305px; top: 18px;
    width: 590px; height: 838px;
    background: var(--paper);
    overflow: hidden;
    box-shadow: 0 4px 18px rgba(0,0,0,0.12);
  }
  .masthead {
    position: absolute; left: 44px; right: 40px; top: 40px;
    display: flex; align-items: center;
  }
  .brand { display: flex; align-items: center; gap: 8px; }
  .brand-dot { width: 14px; height: 14px; border-radius: 50%; background: var(--brand-red); }
  .brand-name {
    font-family: "Lato", Arial, sans-serif;
    font-weight: 700; font-size: 22px; letter-spacing: 1px;
    color: var(--ink);
  }
  .cert-badge {
    margin-left: 28px; width: 56px; height: 34px;
    background: var(--badge);
  }
  .contact {
    margin-left: auto; padding-left: 14px;
    border-left: 1px solid var(--brand-red);
    font-family: "Montserrat", Arial, sans-serif;
    font-style: normal;
    font-size: 8.5px; line-height: 14px; color: var(--muted);
  }
  .contact-row { display: flex; align-items: center; gap: 6px; }
  .contact-row svg { width: 8px; height: 8px; flex: none; }
  .letter {
    position: absolute; left: 70px; top: 150px; width: 410px;
    font-size: 9.5px; line-height: 13px;
  }
  .letter-date { margin-bottom: 14px; }
  .recipient { margin-bottom: 14px; }
  .address { margin-bottom: 20px; }
  .salutation { font-weight: 700; font-size: 12px; margin-bottom: 18px; }
  .letter p.body { margin-bottom: 13px; }
  .closing { margin-top: 20px; }
  .signature {
    font-family: "Great Vibes", cursive;
    font-size: 30px; margin-top: 24px; margin-left: 30px; line-height: 1;
  }
  .corner-band {
    position: absolute; right: 0; bottom: 0;
    width: 230px; height: 250px;
    background: linear-gradient(135deg, var(--brand-blue) 0%, var(--brand-red) 70%);
  }
</style>
</head>
<body>
  <main class="letterhead">
    <header class="masthead">
      <div class="brand">
        <span class="brand-dot"></span>
        <span class="brand-name">MORVEX QSD</span>
      </div>
      <div class="cert-badge" role="img" aria-label="KVSD certification badge"></div>
      <address class="contact">
        <div class="contact-row">
          <svg viewBox="0 0 10 10"><path d="M2 1l2 2-1 1.5c.6 1.2 1.3 1.9 2.5 2.5L7 6l2 2-1.5 1.5C4.5 9 1 5.5.5 2.5z" fill="var(--brand-red)"/></svg>
          555-203-4617
        </div>
        <div class="contact-row">
          <svg viewBox="0 0 10 10"><rect x="0.5" y="2" width="9" height="6" fill="var(--brand-blue)"/><path d="M.5 2l4.5 3.5L9.5 2" stroke="#fff" stroke-width="0.8" fill="none"/></svg>
          Info@Morvex-QSD.com
        </div>
        <div class="contact-row">
          <svg viewBox="0 0 10 10"><circle cx="5" cy="5" r="4.2" fill="none" stroke="var(--brand-red)" stroke-width="1.2"/><path d="M1 5h8M5 1c-2 2.5-2 5.5 0 8M5 1c2 2.5 2 5.5 0 8" stroke="var(--brand-red)" stroke-width="0.7" fill="none"/></svg>
          www.Morvex-QSD.com
        </div>
      </address>
    </header>

    <section class="letter">
      <p class="letter-date">January-03-2020</p>
      <p class="recipient">Mr. Alan Reed<br>President</p>
      <p class="address">Harbor Corporation<br>48 Sample Road, Suite# 10<br>City, State, 120023</p>
      <p class="salutation">Dear Mr. Reed</p>
      <p class="body">Lorem ipsum dolor sit amet, consectetur adipiscing elit, sed do eiusmod tempor incididunt ut labore et dolore magna aliqua. Ut enim ad minim veniam, quis nostrud exercitation ullamco laboris nisi ut aliquip ex ea commodo consequat. Duis aute irure dolor in reprehenderit in voluptate velit esse cillum dolore eu fugiat nulla pariatur.</p>
      <p class="body">Lorem ipsum dolor sit amet, consectetur adipiscing elit, sed do eiusmod tempor incididunt ut labore et dolore magna aliqua. Ut enim ad minim veniam, quis nostrud exercitation ullamco laboris nisi ut aliquip ex ea commodo consequat. Duis aute irure dolor in reprehenderit in voluptate velit esse cillum dolore eu fugiat nulla pariatur.</p>
      <p class="body">Lorem ipsum dolor sit amet, consectetur adipiscing elit, sed do eiusmod tempor incididunt ut labore et dolore magna aliqua. Ut enim ad minim veniam, quis nostrud exercitation ullamco laboris nisi ut aliquip ex ea commodo consequat.</p>
      <p class="body">Excepteur sint occaecat cupidatat non proident, sunt in culpa qui officia deserunt mollit anim id est laborum. re et dolore magnam aliquam quaerat voluptatem.</p>
      <p class="closing">Regards</p>
      <p class="signature">Daniel Price</p>
    </section>

    <div class="corner-band" role="img" aria-label="Decorative red and blue corner band"></div>
  </main>
</body>
</html>
```